you will use Ai to Copy the website Quellabyx.com to come up with the basic frame work and it will give you the understanding of how I would like Zandoprik.com to be like. Zandoprik.com is a peer to peer rv rental site very similar to both of the other rv rental sites the difference is that are commission based 20% and above per rental and we will be one flat monthly rate and they keep all the earnings. Below is photo that will help you with the color scheme and the look and feel of the design

```html
<!DOCTYPE html>
<html lang="en">
<head>
<meta charset="utf-8">
<title>Zandoprik.com — Find an RV for your next adventure</title>
<link href="https://fonts.googleapis.com/css2?family=Outfit:wght@300;400;500;600&display=swap" rel="stylesheet">
<style>
:root{
  --green:#6aa63a;
  --green-dark:#5a9330;
  --navy:#1b2a55;
  --navy-deep:#15224a;
  --ink:#1a1f2e;
  --muted:#4b5063;
  --page:#f6f7fb;
  --white:#ffffff;
  --line:#e3e5ec;
}
*{box-sizing:border-box;margin:0;padding:0}
html,body{width:1200px;height:4155px;overflow:hidden}
body{font-family:'Outfit',sans-serif;color:var(--ink);background:var(--page)}
.page{position:relative;width:1200px;height:4155px;overflow:hidden;background:var(--page)}
.abs{position:absolute}
.swoosh{position:absolute;height:10px}
.swoosh path{fill:none;stroke-width:3;stroke-linecap:round}

/* header */
.brand{left:100px;top:30px;font-size:34px;font-weight:600;color:var(--navy);letter-spacing:-.5px}
.nav a{position:absolute;top:38px;font-size:14px;color:var(--ink);text-decoration:none}
.host-btn{left:911px;top:32px;width:123px;height:31px;border-radius:16px;background:var(--green);color:#fff;font-size:11px;display:flex;align-items:center;justify-content:center}

/* hero */
.hero-title{left:127px;top:150px;font-size:53px;font-weight:500;color:var(--navy);letter-spacing:-.5px}
.search{left:111px;top:258px;width:999px;height:73px;background:#fff;border:1px solid var(--line);border-radius:37px;box-shadow:0 4px 14px rgba(20,30,60,.06)}
.field{position:absolute;top:0;height:73px;padding-top:16px}
.field small{display:block;font-size:11px;color:var(--muted)}
.field span{display:block;font-size:15px;margin-top:4px;color:var(--ink)}
.divider{position:absolute;top:0;width:1px;height:73px;background:var(--line)}
.search-btn{position:absolute;left:933px;top:9px;width:55px;height:55px;border-radius:50%;background:var(--green)}

.promo{top:387px;height:341px;border-radius:4px;overflow:hidden}
.promo-label{position:absolute;left:40px;bottom:22px;color:#fff;font-size:27px;font-weight:500}
.promo-btn{position:absolute;right:22px;bottom:25px;width:95px;height:29px;border-radius:15px;background:#fff;color:var(--ink);font-size:10px;font-weight:500;display:flex;align-items:center;justify-content:center}

/* section heads */
.section-title{font-size:35px;font-weight:500;color:var(--ink)}

.cat{top:881px;width:182px;height:145px;background:#fff;box-shadow:0 3px 12px rgba(20,30,60,.07);text-align:center}
.cat svg{margin-top:28px}
.cat p{font-size:16px;margin-top:12px}

.rv{top:1173px;width:238px;height:305px;background:#fff;box-shadow:0 3px 12px rgba(20,30,60,.05)}
.rv-img{position:absolute;left:22px;top:30px;width:194px;height:155px;border-radius:6px;background:linear-gradient(180deg,#eef0f4,#d9dce3)}
.rv h3{position:absolute;left:27px;top:222px;font-size:18px;font-weight:500}
.rv p{position:absolute;left:27px;top:250px;width:190px;font-size:11px;line-height:16px;color:var(--muted)}

/* split */
.split{top:1557px;height:509px;overflow:hidden;text-align:center;color:#fff}
.split h2{margin-top:66px;font-size:37px;font-weight:400}
.split p{margin-top:30px;font-size:17px;font-weight:300}
.split-btn{position:absolute;top:185px;width:168px;height:39px;border-radius:20px;background:#fff;color:var(--ink);font-size:15px;display:flex;align-items:center;justify-content:center;gap:6px}

.dest{border-radius:2px;overflow:hidden}
.dest span{position:absolute;left:24px;bottom:18px;color:#fff;font-size:20px;font-weight:500}

/* earnings */
.earn-card{left:619px;top:2755px;width:515px;height:332px;background:#fff;box-shadow:0 8px 30px rgba(20,30,60,.1)}
.earn-card h2{position:absolute;left:55px;top:56px;font-size:36px;font-weight:400}
.earn-card p{position:absolute;left:61px;font-size:16px;line-height:23px;color:var(--ink);width:430px}
.navy-btn{position:absolute;left:60px;top:219px;width:169px;height:41px;border-radius:21px;background:var(--navy);color:#fff;font-size:15px;display:flex;align-items:center;justify-content:center;gap:6px}

/* cta */
.cta-title{left:0;width:1220px;top:3335px;text-align:center;font-size:43px;font-weight:400}
.cta-sub{left:0;width:1220px;top:3425px;text-align:center;font-size:22px;line-height:30px;font-weight:300;color:var(--ink)}
.cta-btn{left:476px;top:3511px;width:258px;height:46px;border-radius:23px;background:var(--green);color:#fff;font-size:15px;display:flex;align-items:center;justify-content:center;gap:6px}
.thumb{border-radius:3px}

/* footer */
.footer{left:0;top:3755px;width:1200px;height:400px;background:var(--navy-deep);border-radius:64px 64px 0 0;color:#fff}
.foot-brand{position:absolute;left:106px;top:68px;font-size:30px;font-weight:600;color:#fff}
.social{position:absolute;top:145px;width:25px;height:25px;border-radius:50%;background:#fff}
.col{position:absolute;top:72px}
.col h4{font-size:14px;font-weight:600;margin-bottom:16px}
.col a{display:block;font-size:12.5px;color:#d6dbea;text-decoration:none;line-height:25px}
.foot-line{position:absolute;left:0;top:332px;width:1200px;height:1px;background:rgba(255,255,255,.18)}
.foot-bottom{position:absolute;top:356px;font-size:12px;color:#d6dbea}
</style>
</head>
<body>
<div class="page">

  <!-- header -->
  <div class="abs brand">Zandoprik.com</div>
  <nav class="nav">
    <a style="left:413px">Find an RV</a>
    <a style="left:529px">List Your RV</a>
    <a style="left:653px">How it Works</a>
    <a style="left:786px">Resources</a>
  </nav>
  <div class="abs host-btn">Become a Host</div>
  <svg class="abs" style="left:1052px;top:37px" width="16" height="16" viewBox="0 0 16 16" aria-label="Account"><circle cx="8" cy="5" r="3.5" fill="#1a1f2e"/><path d="M1.5 15c0-4 3-6 6.5-6s6.5 2 6.5 6z" fill="#1a1f2e"/></svg>
  <svg class="abs" style="left:1095px;top:40px" width="20" height="14" viewBox="0 0 20 14" aria-label="Menu"><path d="M0 1h20M0 7h20M0 13h20" stroke="#1a1f2e" stroke-width="2"/></svg>

  <!-- hero -->
  <h1 class="abs hero-title">Find an RV for your next adventure</h1>
  <svg class="swoosh" style="left:721px;top:209px;width:223px;height:14px" viewBox="0 0 223 14"><path d="M2 12 Q110 -2 221 6" stroke="var(--green)"/></svg>

  <div class="abs search">
    <div class="field" style="left:32px"><small>Location</small><span>Amsterdam, NH</span></div>
    <svg style="position:absolute;left:300px;top:32px" width="11" height="11" viewBox="0 0 11 11"><path d="M1 1l9 9M10 1l-9 9" stroke="#9a9fae" stroke-width="1.3"/></svg>
    <div class="divider" style="left:326px"></div>
    <div class="field" style="left:349px"><small>Dates</small><span>Any Dates</span></div>
    <div class="divider" style="left:512px"></div>
    <div class="field" style="left:531px"><small>Guests</small><span>2 guests</span></div>
    <div class="divider" style="left:654px"></div>
    <div class="field" style="left:670px"><small>Driver's age</small><span>25+</span></div>
    <div class="divider" style="left:778px"></div>
    <div class="field" style="left:800px"><small>Rental Type</small><span>All Type</span></div>
    <div class="search-btn">
      <svg width="55" height="55" viewBox="0 0 55 55"><circle cx="26" cy="26" r="7" fill="none" stroke="#fff" stroke-width="2"/><path d="M31 31l6 6" stroke="#fff" stroke-width="2" stroke-linecap="round"/></svg>
    </div>
  </div>

  <div class="abs promo" style="left:124px;width:486px;background:linear-gradient(160deg,#8d8a82 0%,#b9b6ac 40%,#6e7a4e 100%)" role="img" aria-label="Travel trailer towed by a pickup truck beneath desert mountains">
    <div class="promo-label">Drive it or Tow it</div>
    <div class="promo-btn">Book Now</div>
  </div>
  <div class="abs promo" style="left:626px;width:485px;background:linear-gradient(160deg,#3c4a2e 0%,#6b6b5c 45%,#2b3324 100%)" role="img" aria-label="Travel trailer with awning set up at a wooded campsite">
    <div class="promo-label">Delivery &amp; On-Site Stays</div>
    <div class="promo-btn">Pick it up</div>
  </div>

  <!-- browse -->
  <h2 class="abs section-title" style="left:121px;top:800px">Browse RVs visually</h2>
  <svg class="swoosh" style="left:121px;top:850px;width:177px;height:10px" viewBox="0 0 177 10"><path d="M2 8 Q90 0 175 5" stroke="var(--green)"/></svg>
  <svg class="abs" style="left:1024px;top:816px" width="16" height="26" viewBox="0 0 16 26"><path d="M12 3L3 13l9 10" fill="none" stroke="#b4b8c4" stroke-width="2.5"/></svg>
  <svg class="abs" style="left:1078px;top:816px" width="16" height="26" viewBox="0 0 16 26"><path d="M4 3l9 10-9 10" fill="none" stroke="#1a1f2e" stroke-width="2.5"/></svg>

  <div class="abs cat" style="left:118px">
    <svg width="82" height="44" viewBox="0 0 82 44"><g fill="none" stroke="var(--green)" stroke-width="2"><path d="M6 34V14q0-8 10-8h38q10 0 16 14l6 6v8z"/><path d="M12 14h22v10H12zM40 14h14v10H40z"/><circle cx="22" cy="36" r="5"/><circle cx="62" cy="36" r="5"/></g></svg>
    <p>Campervans</p>
  </div>
  <div class="abs cat" style="left:323px">
    <svg width="92" height="44" viewBox="0 0 92 44"><g fill="none" stroke="var(--green)" stroke-width="2"><path d="M4 34V6h80v28z"/><path d="M10 12h18v10H10zM34 12h18v10H34zM62 12h16v10H62zM4 28h80"/><circle cx="20" cy="36" r="5"/><circle cx="68" cy="36" r="5"/></g></svg>
    <p>Class A</p>
  </div>
  <div class="abs cat" style="left:527px">
    <svg width="92" height="44" viewBox="0 0 92 44"><g fill="none" stroke="var(--green)" stroke-width="2"><path d="M4 34V10q0-4 4-4h56q8 0 14 12l8 6v10z"/><path d="M10 12h16v10H10zM32 12h16v10H32zM56 12h12v10H56zM4 28h82"/><circle cx="20" cy="36" r="5"/><circle cx="70" cy="36" r="5"/></g></svg>
    <p>Class B</p>
  </div>
  <div class="abs cat" style="left:732px">
    <svg width="92" height="44" viewBox="0 0 92 44"><g fill="none" stroke="var(--green)" stroke-width="2"><path d="M4 32V14h58V6h24v14H62v12z"/><path d="M10 18h14v8H10zM30 18h14v8H30zM66 10h14v6H66z"/><circle cx="36" cy="36" r="5"/><circle cx="48" cy="36" r="5"/></g></svg>
    <p>Fifth Wheels</p>
  </div>
  <div class="abs cat" style="left:936px">
    <svg width="92" height="44" viewBox="0 0 92 44"><g fill="none" stroke="var(--green)" stroke-width="2"><path d="M8 32V10q0-4 4-4h52q8 0 8 8v18zM72 28h14"/><path d="M14 14h14v10H14zM36 12h10v20H36zM52 14h14v10H52z"/><circle cx="28" cy="36" r="5"/><circle cx="56" cy="36" r="5"/></g></svg>
    <p>Travel Trailers</p>
  </div>

  <!-- near you -->
  <h2 class="abs section-title" style="left:117px;top:1098px">RVs near You</h2>
  <svg class="swoosh" style="left:117px;top:1143px;width:140px;height:10px" viewBox="0 0 140 10"><path d="M2 8 Q70 0 138 5" stroke="var(--green)"/></svg>

  <div class="abs rv" style="left:115px"><div class="rv-img" role="img" aria-label="Pop-top campervan with sliding door open"></div><h3>RV Campervan</h3><p>Lorem ipsum dolor sit amet conse tetur adipiscing lit sed do</p></div>
  <div class="abs rv" style="left:369px"><div class="rv-img" role="img" aria-label="Class A motorhome with slide-outs"></div><h3>RV Campervan</h3><p>Lorem ipsum dolor sit amet conse tetur adipiscing lit sed do</p></div>
  <div class="abs rv" style="left:623px"><div class="rv-img" role="img" aria-label="Class C motorhome"></div><h3>RV Campervan</h3><p>Lorem ipsum dolor sit amet conse tetur adipiscing lit sed do</p></div>
  <div class="abs rv" style="left:876px"><div class="rv-img" role="img" aria-label="Fifth wheel trailer"></div><h3>RV Campervan</h3><p>Lorem ipsum dolor sit amet conse tetur adipiscing lit sed do</p></div>

  <!-- split -->
  <section class="abs split" style="left:0;width:605px;background:linear-gradient(180deg,#6aa63a 0%,#7fae55 35%,#9a9a80 70%,#6b6a5c 100%)" role="img" aria-label="Family sharing a picnic table beside a parked campervan">
    <h2>I want to rent an RV</h2>
    <svg style="position:absolute;left:233px;top:115px" width="140" height="10" viewBox="0 0 140 10"><path d="M2 8 Q70 0 138 5" fill="none" stroke="#fff" stroke-width="3" stroke-linecap="round"/></svg>
    <p>Find the perfect RV for your next getaway.</p>
    <div class="split-btn" style="left:237px">Click here
      <svg width="14" height="12" viewBox="0 0 14 12"><path d="M1 6h11M7 1l5 5-5 5" fill="none" stroke="var(--green)" stroke-width="1.8"/></svg></div>
  </section>
  <section class="abs split" style="left:608px;width:592px;background:linear-gradient(180deg,#1b2a55 0%,#2a3f6e 40%,#8a97a8 70%,#a79e82 100%)" role="img" aria-label="Class C motorhome parked on desert plains with mountains behind">
    <h2>I want to list my RV</h2>
    <svg style="position:absolute;left:226px;top:115px" width="140" height="10" viewBox="0 0 140 10"><path d="M2 8 Q70 0 138 5" fill="none" stroke="#fff" stroke-width="3" stroke-linecap="round"/></svg>
    <p>Turn your RV into an income opportunity.</p>
    <div class="split-btn" style="left:219px">Click here
      <svg width="14" height="12" viewBox="0 0 14 12"><path d="M1 6h11M7 1l5 5-5 5" fill="none" stroke="var(--green)" stroke-width="1.8"/></svg></div>
  </section>

  <!-- destinations -->
  <h2 class="abs section-title" style="left:116px;top:2143px">Explore Popular Destinations</h2>
  <svg class="swoosh" style="left:371px;top:2186px;width:202px;height:10px" viewBox="0 0 202 10"><path d="M2 8 Q100 0 200 5" stroke="var(--green)"/></svg>

  <div class="abs dest" style="left:115px;top:2226px;width:493px;height:368px;background:linear-gradient(150deg,#4f86b3 0%,#5f7d4e 40%,#8b6a4c 75%,#6d6f70 100%)" role="img" aria-label="Coastal highway bridge along rugged California cliffs"><span style="font-size:29px;left:36px;bottom:24px">California</span></div>
  <div class="abs dest" style="left:624px;top:2226px;width:241px;height:174px;background:linear-gradient(180deg,#8fb6d8 0%,#6d7f72 50%,#4c5f6e 100%)" role="img" aria-label="Mountain town beside a lake in Colorado"><span>Colorado</span></div>
  <div class="abs dest" style="left:879px;top:2226px;width:242px;height:174px;background:linear-gradient(180deg,#b49aa8 0%,#b05b3a 50%,#6b3b28 100%)" role="img" aria-label="Red rock buttes in Arizona at sunset"><span>Arizona</span></div>
  <div class="abs dest" style="left:624px;top:2416px;width:241px;height:178px;background:linear-gradient(180deg,#a8c4dc 0%,#6d8aa0 45%,#4d6a5a 100%)" role="img" aria-label="Florida coastline with beachfront towers"><span>Florida</span></div>
  <div class="abs dest" style="left:879px;top:2416px;width:242px;height:178px;background:linear-gradient(180deg,#6d95c4 0%,#a05a3e 55%,#5e4a38 100%)" role="img" aria-label="Sedona red rock formations under blue sky"><span>Sedona</span></div>

  <!-- earnings -->
  <div class="abs" style="left:108px;top:2692px;width:650px;height:465px;background:linear-gradient(180deg,#9dbde0 0%,#5f7f6a 40%,#2f4a2e 70%,#5d6066 100%)" role="img" aria-label="Two motorhomes driving a winding road through pine forest and mountains"></div>
  <div class="abs earn-card">
    <h2>Your RV Your Earnings.</h2>
    <svg style="position:absolute;left:263px;top:101px" width="145" height="10" viewBox="0 0 145 10"><path d="M2 8 Q72 0 143 5" fill="none" stroke="var(--green)" stroke-width="3" stroke-linecap="round"/></svg>
    <p style="top:118px">Why give away a large percentage of every rental?</p>
    <p style="top:150px">Zandoprik.com offers RV owners a simpler alternative to commission-based rental marketplaces.</p>
    <div class="navy-btn">Click here
      <svg width="14" height="12" viewBox="0 0 14 12"><path d="M1 6h11M7 1l5 5-5 5" fill="none" stroke="#fff" stroke-width="1.8"/></svg></div>
  </div>

  <!-- cta -->
  <div class="abs thumb" style="left:89px;top:3278px;width:180px;height:114px;background:linear-gradient(160deg,#4a5a3a,#8d8f86)" role="img" aria-label="Travel trailer with awning at a campsite"></div>
  <div class="abs thumb" style="left:924px;top:3263px;width:174px;height:135px;background:linear-gradient(160deg,#9fb1c2,#6e7468)" role="img" aria-label="White motorhome parked in a mountain pass"></div>
  <div class="abs thumb" style="left:202px;top:3534px;width:164px;height:115px;background:linear-gradient(160deg,#d9a26a,#5a4a42)" role="img" aria-label="Motorhome on a road at sunset"></div>
  <div class="abs thumb" style="left:842px;top:3526px;width:227px;height:127px;background:linear-gradient(180deg,#7d8fa3,#7e8a52)" role="img" aria-label="Camper van parked on grassy field"></div>

  <h2 class="abs cta-title">Ready to Start Your Journey?</h2>
  <svg class="swoosh" style="left:524px;top:3384px;width:170px;height:10px" viewBox="0 0 170 10"><path d="M2 8 Q85 0 168 5" stroke="var(--green)"/></svg>
  <p class="abs cta-sub">Find your next RV or turn the one you own into an<br>earning opportunity.</p>
  <div class="abs cta-btn">Find an RV List Your RV
    <svg width="14" height="12" viewBox="0 0 14 12"><path d="M1 6h11M7 1l5 5-5 5" fill="none" stroke="#fff" stroke-width="1.8"/></svg></div>

  <!-- footer -->
  <footer class="abs footer">
    <div class="foot-brand">Zandoprik.com</div>
    <span class="social" style="left:119px" aria-label="Social link"></span>
    <span class="social" style="left:156px" aria-label="Social link"></span>
    <span class="social" style="left:191px" aria-label="Social link"></span>
    <span class="social" style="left:228px" aria-label="Social link"></span>
    <span class="social" style="left:265px" aria-label="Social link"></span>

    <div class="col" style="left:398px"><h4>Navigation</h4><a>Where it all began</a><a>Careers</a><a>Stories and news</a><a>Travel journal</a><a>About</a></div>
    <div class="col" style="left:594px"><h4>Guest travel</h4><a>Group bookings</a><a>National park guides</a><a>One-way rentals</a><a>Road trip guides</a><a>RV parks &amp; campgrounds</a><a>Guide to all RV types</a></div>
    <div class="col" style="left:810px"><h4>Hosting</h4><a>Become an RV host</a><a>Fleetdesk demo</a><a>Affiliate program</a><a>RV insurance</a><a>Host Pomelo app</a><a>Host Tarnix app</a></div>
    <div class="col" style="left:1005px"><h4>Support</h4><a>How it works</a><a>Help center</a><a>LLM info</a><a>Contact</a></div>

    <div class="foot-line"></div>
    <div class="foot-bottom" style="left:113px">© 2026 Zandoprik.com. All rights reserved.</div>
    <div class="foot-bottom" style="left:922px">Terms &nbsp;|&nbsp; Privacy &nbsp;|&nbsp; Sitemap</div>
  </footer>
</div>
</body>
</html>
```